I need a brochure design to my company Marion Tessaud Coaching. I am personal trainer for VIP, on the web www.mariontessaud.com and I've got a team of trainers. I develop my business for companies to help them to manage the stress of their people. I send trainers to give yoga classes in the open space of the employees. I want to see : professionalism, fresh attitude, colors, health. The final design should communicate professional and fresh ! Here is my logo, that I would love to see in a different color to make the difference with my website. Same logo, different color to make think, I am talking to companies and notre private client.

Industry/Entity Type

Personal Trainer

```html
<!DOCTYPE html>
<html lang="en">
<head>
<meta charset="utf-8">
<title>Marion Tessaud Coaching – Brochure</title>
<link href="https://fonts.googleapis.com/css2?family=Source+Sans+3:wght@400;600;700&display=swap" rel="stylesheet">
<style>
  :root {
    --pink: #e8176f;
    --blush: #f9d2e7;
    --blush-deep: #f3b3d6;
    --aqua: #7fe6e0;
    --aqua-band: #86ebe8;
    --ink: #111111;
    --white: #ffffff;
  }
  * { margin: 0; padding: 0; box-sizing: border-box; }
  html, body { width: 846px; height: 1200px; overflow: hidden; background: var(--white); }
  body { font-family: "Source Sans 3", Arial, sans-serif; }

  .brochure { position: relative; width: 846px; height: 1200px; overflow: hidden; background: var(--white); }

  /* Header */
  .masthead { position: absolute; inset: 0 0 auto 0; height: 290px; }
  .masthead svg { position: absolute; inset: 0; width: 846px; height: 290px; }
  .brand-dot {
    position: absolute; left: 40px; top: 22px; width: 164px; height: 164px;
    border-radius: 50%; background: var(--aqua);
  }
  .brand-name {
    position: absolute; left: 232px; top: 38px;
    font-size: 84px; font-weight: 400; color: var(--pink); letter-spacing: -1px; line-height: 1;
  }
  .tagline {
    position: absolute; left: 252px; top: 132px;
    font-size: 25px; font-weight: 600; color: var(--pink);
  }

  /* Feature rows */
  .feature-photo {
    position: absolute; width: 228px; height: 228px; border-radius: 50%;
    border: 6px solid var(--aqua);
  }
  .photo-yoga-beach { left: 58px; top: 284px; background: linear-gradient(160deg, #8fc3ea 0%, #b9d7ee 45%, #d9c9a6 70%, #c6b38e 100%); }
  .photo-crowd { left: 552px; top: 528px; background: linear-gradient(170deg, #c9bfb4 0%, #a79283 50%, #6f5b51 100%); }
  .photo-park-class { left: 58px; top: 776px; background: linear-gradient(180deg, #8ca37a 0%, #6f8d58 40%, #a88f92 65%, #5f8a3e 100%); }

  .feature-copy { position: absolute; width: 480px; }
  .feature-copy h2 {
    font-size: 64px; font-weight: 400; color: var(--pink); line-height: 1; letter-spacing: -0.5px;
  }
  .feature-copy h2 strong { font-weight: 700; }
  .feature-copy p {
    margin-top: 4px; font-size: 22px; font-weight: 600; color: var(--ink); line-height: 29px;
  }
  .copy-one { left: 332px; top: 300px; }
  .copy-two { left: 38px; top: 544px; }
  .copy-three { left: 332px; top: 792px; }

  /* Footer */
  .contact-band {
    position: absolute; left: 0; right: 0; top: 1010px; height: 190px;
    background: var(--aqua-band); color: var(--pink); font-weight: 700; font-size: 25px;
  }
  .contact-band span { position: absolute; white-space: nowrap; line-height: 1; }
  .web { left: 284px; top: 22px; }
  .mail { left: 26px; top: 58px; }
  .phone { left: 532px; top: 58px; }
  .page { left: 154px; top: 102px; }
  .handle-one { left: 26px; top: 146px; }
  .handle-two { left: 300px; top: 146px; }
  .handle-three { left: 546px; top: 146px; }
  .dot { display: inline-block; width: 18px; height: 18px; border-radius: 50%; background: var(--pink); margin-right: 6px; vertical-align: -1px; }
</style>
</head>
<body>
<main class="brochure">
  <header class="masthead">
    <svg viewBox="0 0 846 290" aria-hidden="true">
      <defs>
        <linearGradient id="headerFill" x1="0" y1="0" x2="0" y2="1">
          <stop offset="0" stop-color="#fbe3f0"/>
          <stop offset="1" stop-color="#f6c6e0"/>
        </linearGradient>
      </defs>
      <path d="M0 0 H846 V238 C720 214 600 214 470 236 C330 262 180 272 0 240 Z" fill="url(#headerFill)"/>
      <path d="M0 240 C180 272 330 262 470 236 C600 214 720 214 846 238 V252 C720 230 600 232 470 252 C330 276 180 284 0 256 Z" fill="var(--blush-deep)"/>
    </svg>
    <div class="brand-dot"></div>
    <h1 class="brand-name">MarionTessaud</h1>
    <p class="tagline">Yoga - Stress Relief - Positive Work Culture</p>
  </header>

  <section>
    <div class="feature-photo photo-yoga-beach" role="img" aria-label="Photo of a woman in a yoga side-plank pose on a sunny beach"></div>
    <div class="feature-copy copy-one">
      <h2>Lorem <strong>Ipsum</strong></h2>
      <p>Lorem ipsum dolor sit amet, consectetur<br>adipiscing elit. Sed tincidunt eleifend eros,<br>et blandit sapien lacinia eu. Quisque<br>gravida leo in rhoncus maximus.</p>
    </div>
  </section>

  <section>
    <div class="feature-copy copy-two">
      <h2>Lorem <strong>Ipsum</strong></h2>
      <p>Lorem ipsum dolor sit amet, consectetur<br>adipiscing elit. Sed tincidunt eleifend eros,<br>et blandit sapien lacinia eu. Quisque<br>gravida leo in rhoncus maximus.</p>
    </div>
    <div class="feature-photo photo-crowd" role="img" aria-label="Photo of a crowd of people with raised arms"></div>
  </section>

  <section>
    <div class="feature-photo photo-park-class" role="img" aria-label="Photo of a group yoga class on the grass in a park"></div>
    <div class="feature-copy copy-three">
      <h2>Lorem <strong>Ipsum</strong></h2>
      <p>Lorem ipsum dolor sit amet, consectetur<br>adipiscing elit. Sed tincidunt eleifend eros,<br>et blandit sapien lacinia eu. Quisque<br>gravida leo in rhoncus maximus.</p>
    </div>
  </section>

  <footer class="contact-band">
    <span class="web">www.mariontessaud.com</span>
    <span class="mail">contact@mariontessaud.com</span>
    <span class="phone">+33 (0)9 48 22 15 30</span>
    <span class="page"><i class="dot"></i>- pages/Marion-Tessaud/208716453390125</span>
    <span class="handle-one"><i class="dot"></i>- MARIONTESSAUD</span>
    <span class="handle-two"><i class="dot"></i>- mariontessaud/</span>
    <span class="handle-three"><i class="dot"></i>- user/MarionTessaud</span>
  </footer>
</main>
</body>
</html>
```